Law Firm Website

I currently have a temporary site that I created myself at www.mcorveyfirm.net (hosted by 9tree). I am generally happy with the content.

My permanent website just has basic information right now: www.mcorveyfirm.com (hosted by lumenrack). I want to take the general content from the temporary website and have a more professional looking website on the permanent website. I want it in Wordpress format. I want a link to my blog: www.crookedpath.com. I want it to work on pads and smart phones. My number and e-mail address should be available on every page. The idea is to feature the potential client more than the lawyer.
Updates

Several of the designs are good. I would like the front page to have my number and address at the top (and at the top of every page) and to identify my law firm as "Law Office of Gerald T. Corvey". No need to include "mcorveyfirm" as that is just the web address. I like showing the most recent blog posts on the front page. I don't need video. No need to emphasize office hours or map location on the front page (that could be under a contact button). My picture should be somewhere. I would like an image from Boston on the front page if we can find one that is not copyright protected. No images of gavels or scales of justice. See some of the sample websites I listed in previous messages. Thanks!

Industry/Entity Type

Law Firm

```html
<!DOCTYPE html>
<html lang="en">
<head>
<meta charset="utf-8">
<title>Law Office of Gerald T. Corvey</title>
<link rel="stylesheet" href="https://fonts.googleapis.com/css2?family=Comfortaa:wght@300;400&family=Roboto+Condensed:wght@400&family=Roboto:wght@400&family=Open+Sans:ital,wght@0,400;0,600;0,700;1,700&family=Ubuntu:wght@300;400;500;700&display=swap">
<style>
:root{
  --bg-deep:#06507a;
  --bg-mid:#1490c4;
  --bar-dark:#333333;
  --page:#f5f7f8;
  --nav-top:#1a8fc4;
  --nav-bottom:#075a8c;
  --hero:#0f86bd;
  --yellow:#f7e21a;
  --gold:#f2a900;
  --accent:#1a9bc7;
  --ink:#2f2f2f;
  --muted:#5b6867;
  --green:#1a6b4a;
  --link:#0e5e87;
  --footer:#161a1d;
}
*{box-sizing:border-box;margin:0;padding:0}
html,body{width:893px;height:1200px;overflow:hidden}
body{position:relative;background:radial-gradient(ellipse at 50% 40%,var(--bg-mid) 0%,#0a6da0 55%,var(--bg-deep) 100%);font-family:"Open Sans",sans-serif;color:var(--ink)}
.abs{position:absolute;white-space:normal}
.topbar{left:0;top:0;width:893px;height:27px;background:var(--bar-dark)}
.get-connected{left:662px;top:6px;font:600 10.5px/14px "Open Sans",sans-serif;color:#d0d0d0;white-space:nowrap}
.social{top:6px;width:15px;height:15px;background:#9a9a9a;border-radius:2px}
.page{left:62px;top:27px;width:768px;height:1083px;background:var(--page)}
.logo-disc{left:92px;top:6px;width:68px;height:68px;border-radius:50%;background:var(--page)}
.brand{left:108px;top:30px;font:300 35px "Comfortaa",sans-serif;color:var(--accent);letter-spacing:-.5px;white-space:nowrap}
.brand-sub{left:112px;top:70px;font:300 13px "Comfortaa",sans-serif;color:var(--muted);white-space:nowrap}
.phone-icon{left:644px;top:56px;width:27px;height:27px;border-radius:5px;background:#111}
.phone-number{left:679px;top:54px;font:400 24px "Roboto",sans-serif;color:#222;white-space:nowrap}
.nav{left:69px;top:112px;width:754px;height:46px;background:linear-gradient(var(--nav-top),var(--nav-bottom));border-top:2px solid #0b5f8f;border-bottom:3px solid #053f63}
.nav-tab{left:74px;top:121px;width:58px;height:36px;background:linear-gradient(#fff,#e6e9ea);border-radius:10px 10px 0 0}
.nav-link{top:128px;font:400 11.5px/14px "Roboto Condensed",sans-serif;color:#fff;white-space:nowrap}
.nav-link.current{color:var(--accent);left:74px;width:58px;text-align:center}
.hero{left:69px;top:166px;width:754px;height:269px;background:linear-gradient(90deg,#0c7bb0,var(--hero) 60%,#0a6a9e)}
.hero-frame{left:82px;top:175px;width:469px;height:248px;background:#fff;box-shadow:0 1px 4px rgba(0,0,0,.4)}
.hero-photo{left:89px;top:182px;width:455px;height:234px;background:radial-gradient(ellipse at 50% 45%,#b9c4c6,#6d7d80 70%,#3e4a4d)}
.overview-title{left:568px;top:174px;width:242px;text-align:center;font:700 27px "Ubuntu",sans-serif;color:var(--yellow)}
.overview-text{left:567px;top:213px;width:244px;font-size:9.6px;line-height:16.3px;color:#fff;text-align:justify}
.btn{left:619px;top:390px;width:139px;height:29px;background:linear-gradient(#ffe22b,#f2b800);font:700 16px "Open Sans",sans-serif;color:#2b2200;text-align:center;line-height:29px}
.welcome{left:76px;top:458px;font:500 19px "Ubuntu",sans-serif;color:var(--muted);white-space:nowrap}
.rule{height:0;border-top:1px dotted #cfd6d8}
.portrait-frame{left:86px;top:502px;width:105px;height:127px;background:#fff;box-shadow:0 1px 3px rgba(0,0,0,.25)}
.portrait{left:92px;top:507px;width:94px;height:116px;background:linear-gradient(#5e4a3c,#2c2f36)}
.intro{left:221px;top:506px;width:343px;font-size:9.7px;line-height:17px;text-align:justify}
.more{font:700 9.5px "Open Sans",sans-serif;color:var(--green);white-space:nowrap}
.more::after{content:" \25B8"}
.tagline{left:86px;top:672px;width:480px;font:300 15.5px/20px "Ubuntu",sans-serif;color:var(--accent);text-align:justify}
.body-copy{left:87px;top:741px;width:479px;font-size:9.7px;line-height:15.6px;text-align:justify}
.recent-title{left:86px;top:851px;font:700 17.5px "Ubuntu",sans-serif;color:var(--muted)}
.view-all{left:505px;top:859px;font:700 8.5px "Open Sans",sans-serif;color:var(--link)}
.post{left:74px;top:883px;width:490px;height:207px;background:#e9ebeb}
.post-title{left:88px;top:897px;width:460px;font:700 12px/14px "Open Sans",sans-serif;color:var(--gold)}
.post-by{left:300px;top:927px;width:232px;text-align:right;font:italic 700 9.5px "Open Sans",sans-serif;color:var(--accent)}
.post-text{left:89px;width:458px;font-size:9.8px;line-height:14px;text-align:justify}
.posted{left:92px;top:1059px;font:600 8.5px "Open Sans",sans-serif;color:var(--muted)}
.posted em{font-weight:700;color:var(--green)}
.side-card{left:599px;width:223px;background:#fff;box-shadow:0 0 3px rgba(0,0,0,.25)}
.contact-box{left:606px;top:459px;width:210px;height:301px;background:radial-gradient(ellipse at 50% 30%,#1ea4dc,#0b77b5 60%,#06558d)}
.contact-box .t{position:absolute;left:9px;color:#fff;font-size:9.5px;line-height:14px;white-space:nowrap}
.ci-title{left:606px;top:467px;width:210px;text-align:center;font:700 13px "Ubuntu",sans-serif;color:var(--yellow)}
.hours-title{left:606px;top:681px;width:210px;text-align:center;font:700 13.5px "Ubuntu",sans-serif;color:#fff}
.pres-box{left:606px;top:806px;width:210px;height:204px;background:#eceeee}
.pres-title{left:606px;top:813px;width:210px;text-align:center;font:700 12.5px "Ubuntu",sans-serif;color:var(--accent)}
.pres-photo{left:632px;top:844px;width:155px;height:76px;background:linear-gradient(90deg,#8a6b45,#d9d1c0 50%,#6a543d)}
.pres-text{left:614px;top:929px;width:196px;font-size:9.2px;line-height:14px;color:#333;text-align:justify}
.footer{left:53px;top:1098px;width:787px;height:110px;background:var(--footer);border-radius:8px 8px 0 0}
.foot-nav{left:53px;top:1120px;width:787px;text-align:center;font-size:9px;color:#e6e6e6;word-spacing:1px;white-space:nowrap}
.foot-nav span{margin:0 7px;color:#bbb}
.foot-name{left:53px;top:1146px;width:787px;text-align:center;font:italic 700 11px "Open Sans",sans-serif;color:#fff}
.foot-line{left:53px;width:787px;text-align:center;font-size:9px;color:#fff;white-space:nowrap}
</style>
</head>
<body>
<div class="abs topbar"></div>
<div class="abs get-connected">Get Connected</div>
<div class="abs social" role="img" aria-label="Social profile" style="left:747px"></div>
<div class="abs social" role="img" aria-label="Social profile" style="left:770px"></div>
<div class="abs social" role="img" aria-label="Social profile" style="left:793px"></div>

<div class="abs page"></div>
<div class="abs logo-disc"></div>
<div class="abs brand">Gerald T. Corvey</div>
<div class="abs brand-sub">Law Office of Gerald T. Corvey</div>
<svg class="abs phone-icon" viewBox="0 0 27 27" aria-label="Phone">
  <path d="M10 6c-2 1-3 3-3 7s2 8 5 9c1 0 2-1 3-2l-2-3-2 1c-1-2-1-5 0-7l2 0 1-4z" fill="#fff"/>
</svg>
<div class="abs phone-number">617 555-0142</div>

<nav>
  <div class="abs nav"></div>
  <div class="abs nav-tab"></div>
  <a class="abs nav-link current">Home</a>
  <a class="abs nav-link" style="left:142px">Why Hire Me?</a>
  <a class="abs nav-link" style="left:234px">Success Stories</a>
  <a class="abs nav-link" style="left:333px">Practice Areas</a>
  <a class="abs nav-link" style="left:425px">Representative Clients</a>
  <a class="abs nav-link" style="left:553px">Services Provided</a>
  <a class="abs nav-link" style="left:662px">Contact Us</a>
  <a class="abs nav-link" style="left:738px">How To Find Us</a>
</nav>

<section>
  <div class="abs hero"></div>
  <div class="abs hero-frame"></div>
  <div class="abs hero-photo" role="img" aria-label="Businessman in a suit holding open hands beneath a crowd of client figures over a world map"></div>
  <h2 class="abs overview-title">OVERVIEW</h2>
  <p class="abs overview-text">Lorem Ipsum is simply dummy text of the printing and typesetting industry. Lorem Ipsum has been the industry's standard dummy text ever since the 1500s, when an unknown printer took a galley of type and scrambled it to make a type specimen book. It has survived not only five centuries, but also the leap into electronic typesetting, remaining essentially unchanged. It was popularised in the 1960s with the release of Setraform sheets containing Lorem Ipsum passages...</p>
  <div class="abs btn">More Details</div>
</section>

<main>
  <h1 class="abs welcome">Welcome to the Law Office of Gerald T. Corvey</h1>
  <div class="abs rule" style="left:74px;top:491px;width:494px"></div>
  <div class="abs portrait-frame"></div>
  <div class="abs portrait" role="img" aria-label="Portrait of the attorney"></div>
  <p class="abs intro">I give real, practical advice to keep you out of trouble, stay in business and make money. I won't bore you with legal theories, but will explain how the legal issues affect your business. I have a passion for helping businesses and other clients. If you are sued or have to sue another business, customer or ex-employee or business partner, I will develop the right, cost effective strategy with you.</p>
  <div class="abs more" style="left:498px;top:625px">More Details</div>
  <div class="abs rule" style="left:74px;top:653px;width:502px"></div>

  <h2 class="abs tagline">Protecting and Defending Your Business Against Competitors, Rogue Employees, Cheating Business Partners, Devious Contracting Parties, and Overzealous Government Agencies.</h2>
  <p class="abs body-copy">Your business is under constant attack.&nbsp; With more success, you become more of a target. Whether it's keeping you out of a lawsuit or defending one that you are already in (or prosecuting one when necessary), I'm here to help.<br>Don't settle for lawyers who promise to work to solve your problems.&nbsp; I will work to prevent your problems in the first place.&nbsp; Learn more about litigation avoidance in my practice areas of law.</p>
  <div class="abs rule" style="left:74px;top:842px;width:502px"></div>

  <h2 class="abs recent-title">Recent Post</h2>
  <div class="abs view-all">View All [+]</div>
  <article>
    <div class="abs post"></div>
    <h3 class="abs post-title">You're Damned If You Don't Respond Appropriately to a Poor ReviewHub Review or Online Post.</h3>
    <div class="abs post-by">By Gerald T. Corvey 617.555.0142</div>
    <p class="abs post-text" style="top:951px">We are offering this incredible 5BR+/6.5BA Pool Home with Mother-in-Law Suite situated on a stately 2.28± acres in the very private, and very exclusive Mountain Lake community. Click through for Photos and details on this wonderful opportunity.</p>
    <p class="abs post-text" style="top:1007px">There are a variety of options for employee parties, from providing the liquor yourself at the company premises, having a professional caterer on the premises, renting a function hall, or going to a bar or restaurant. Some of these are safer options than others.</p>
    <div class="abs posted"><em>Posted:</em>&nbsp; December 19, 2013&nbsp; in Uncategorized</div>
    <div class="abs more" style="left:476px;top:1058px;color:var(--link)">More Details</div>
  </article>
</main>

<aside>
  <div class="abs side-card" style="top:453px;height:315px"></div>
  <div class="abs contact-box">
    <div class="t" style="top:43px;font:700 12px 'Open Sans',sans-serif">Law Office of Gerald T. Corvey</div>
    <div class="t" style="top:68px">48 Harlow St., 3rd Floor<br>Boston, MA 02110-1400</div>
    <div class="t" style="top:109px">Phone: 617 555-0142<br>Fax: 857 555-0193<br>Email: gcorvey@mcorveyfirm.com<br>Blog: www.crookedpath.com</div>
    <div class="t" style="top:180px">Or use our <b><i><u>contact form</u></i></b>.</div>
    <div class="t" style="top:246px;left:8px;font-size:8.8px">We can be reached during the following hours</div>
    <div class="t" style="top:263px;left:12px;font:italic 700 12px 'Open Sans',sans-serif;color:#3cc6f5">Monday Thru Friday <span style="font-style:normal;color:#2fd0ff">10am-6pm</span></div>
  </div>
  <svg class="abs" style="left:614px;top:470px" width="196" height="12" aria-hidden="true">
    <path d="M2 6h18M14 2l6 4-6 4M176 6h18M182 2l-6 4 6 4" stroke="#fff" stroke-width="1.3" fill="none"/>
  </svg>
  <h3 class="abs ci-title">CONTACT INFO</h3>
  <h3 class="abs hours-title">OFFICE HOURS</h3>

  <div class="abs side-card" style="top:798px;height:218px"></div>
  <div class="abs pres-box"></div>
  <svg class="abs" style="left:611px;top:816px" width="200" height="12" aria-hidden="true">
    <path d="M2 6h18M14 2l6 4-6 4M180 6h18M186 2l-6 4 6 4" stroke="#5b6867" stroke-width="1.3" fill="none"/>
  </svg>
  <h3 class="abs pres-title">ONLINE PRESENTATIONS</h3>
  <div class="abs pres-photo" role="img" aria-label="Business people walking through a bright office lobby"></div>
  <p class="abs pres-text">A recent study shows that plaintiffs in most diversity cases never asked a judge to "certify a class" of those covered in the suit. ...</p>
  <svg class="abs" style="left:777px;top:988px" width="28" height="14" aria-label="Previous and next">
    <path d="M7 2l-5 5 5 5" stroke="#8fb3c2" stroke-width="2.2" fill="none"/>
    <path d="M20 2l5 5-5 5" stroke="#0b4f7d" stroke-width="2.2" fill="none"/>
  </svg>
</aside>

<footer>
  <div class="abs footer"></div>
  <div class="abs foot-nav">Home<span>|</span>Why Hire Me?<span>|</span>Success Stories<span>|</span>Practice Areas<span>|</span>Representative Clients<span>|</span>Services Provided<span>|</span>Contact Us<span>|</span>How To Find Us</div>
  <div class="abs foot-name">Law Office of Gerald T. Corvey</div>
  <div class="abs foot-line" style="top:1163px">Phone: 617 555-0142, Fax: 857 555-0193,&nbsp; Email: gcorvey@mcorveyfirm.com, Blog: www.crookedpath.com</div>
  <div class="abs foot-line" style="top:1184px">© Law Office of Gerald T. Corvey , Sitemap</div>
</footer>
</body>
</html>
```